Bold Plum

I am starting a sharpening service for knives, scissors, and garden tools. It's a sole proprietorship, so it's a small business. The business name is "Bolt Plum." A one or two-page website is fine. Ember Guild has created a logo for me. There should be pictures of the things I sharpen. There will also be a price list for sharpened items. My address is: 18392 Calloway Lane, Stevenson Ranch, CA 91307. Phone number is 661-555-0172

```html
<!DOCTYPE html>
<html lang="en">
<head>
<meta charset="utf-8">
<title>Bolt Plum — Sharpening Service</title>
<link href="https://fonts.googleapis.com/css2?family=Audiowide&family=Mulish:wght@400;500;600;700;800&display=swap" rel="stylesheet">
<style>
:root{
  --ink:#0d111a;
  --navy:#161c29;
  --navy-2:#1d2535;
  --white:#ffffff;
  --paper:#f2f2f2;
  --line:#d6d6d6;
  --muted:#555b66;
  --steel:#9aa0a8;
  --ember:#e07a22;
}
*{box-sizing:border-box;margin:0;padding:0}
html,body{width:1200px;height:3873px;overflow:hidden}
body{position:relative;background:var(--white);font-family:'Mulish',sans-serif;color:var(--ink)}
.abs{position:absolute}
.display{font-family:'Audiowide',sans-serif;letter-spacing:3px;text-transform:uppercase;font-weight:400}
.btn{position:absolute;display:flex;align-items:center;justify-content:center;gap:8px;font-weight:800;font-size:15px;border-radius:6px;text-transform:uppercase}
.btn svg{width:14px;height:14px}
.btn-dark{background:var(--ink);color:var(--white)}
.btn-light{background:var(--white);color:var(--ink)}
.mark{position:absolute;width:56px;height:56px;border-radius:50%;background:var(--steel)}
.eyebrow{position:absolute;font-size:20px;font-weight:500;text-transform:uppercase;left:0;width:1200px;text-align:center}
.title-center{position:absolute;left:0;width:1200px;text-align:center;font-size:37px;letter-spacing:4px}

/* nav */
.nav{position:absolute;left:0;top:0;width:1200px;height:93px;background:var(--white)}
.brand{position:absolute;left:152px;top:24px;display:flex;align-items:center;gap:12px;font-weight:800;font-size:32px;color:var(--ink)}
.brand-dot{width:34px;height:34px;background:var(--ink);border-radius:50%}
.nav-link{position:absolute;top:32px;font-size:16px;font-weight:500}

/* hero */
.hero{position:absolute;left:0;top:93px;width:1200px;height:578px;background:var(--navy)}
.hero-photo{position:absolute;left:560px;top:0;width:640px;height:578px;
  background:
    linear-gradient(90deg,var(--navy) 0%,rgba(22,28,41,.6) 14%,rgba(22,28,41,0) 32%),
    radial-gradient(ellipse 14% 14% at 34% 76%,rgba(190,30,40,.75),transparent 70%),
    radial-gradient(ellipse 12% 10% at 44% 60%,rgba(150,170,90,.55),transparent 70%),
    radial-gradient(ellipse 11% 10% at 70% 58%,rgba(150,170,90,.55),transparent 70%),
    radial-gradient(ellipse 10% 14% at 52% 24%,rgba(170,120,95,.7),transparent 70%),
    radial-gradient(ellipse 30% 40% at 62% 45%,#22304e,transparent 75%),
    radial-gradient(ellipse 10% 20% at 92% 20%,rgba(180,30,30,.6),transparent 70%),
    linear-gradient(180deg,#4c4440 0%,#3a3431 60%,#2a2420 78%,#1c1815 100%)}
.hero h1{position:absolute;left:153px;top:150px;font-size:41px;line-height:54px;color:var(--white);letter-spacing:4px}
.hero p{position:absolute;left:151px;top:280px;width:400px;font-size:15px;line-height:26px;color:var(--white)}

/* about */
.about-photo{position:absolute;left:150px;top:734px;width:394px;height:487px;border-radius:20px;
  background:
    radial-gradient(ellipse 16% 10% at 30% 83%,rgba(255,200,80,.95),rgba(224,122,34,.5) 45%,transparent 75%),
    radial-gradient(ellipse 18% 16% at 62% 22%,rgba(190,120,80,.6),transparent 70%),
    radial-gradient(ellipse 28% 32% at 70% 50%,rgba(150,140,120,.45),transparent 70%),
    radial-gradient(ellipse 40% 30% at 20% 15%,rgba(200,110,40,.45),transparent 70%),
    linear-gradient(180deg,#3a2818 0%,#241a13 45%,#1a1410 75%,#2c2a28 100%)}
.about-copy{position:absolute;left:605px;width:440px}
.about-copy p{font-size:13px;line-height:19px;color:var(--muted);text-align:justify}

/* services */
.services{position:absolute;left:0;top:1313px;width:1200px;height:758px;background:linear-gradient(180deg,var(--navy-2),var(--navy))}
.card{position:absolute;width:289px;height:369px;background:var(--white);border-radius:18px}
.card .img{position:absolute;left:8px;top:8px;width:273px;height:299px;border-radius:14px}
.card .label{position:absolute;left:0;bottom:22px;width:100%;text-align:center;font-size:15px;letter-spacing:2px}
.card.featured{border:4px solid var(--white);background:transparent;overflow:hidden;box-shadow:0 0 0 3px rgba(255,255,255,.35)}
.card.featured .img{left:4px;top:4px;width:273px;height:353px;
  background:
    radial-gradient(ellipse 30% 22% at 45% 55%,rgba(240,150,60,.55),transparent 70%),
    radial-gradient(ellipse 18% 14% at 75% 35%,rgba(130,110,100,.45),transparent 70%),
    radial-gradient(ellipse 50% 30% at 50% 95%,rgba(120,70,40,.6),transparent 70%),
    linear-gradient(180deg,#23262e 0%,#2b2a2c 55%,#1e1a18 100%)}
.featured-text{position:absolute;left:0;top:130px;width:100%;text-align:center;color:var(--white)}
.featured-text h3{font-family:'Audiowide',sans-serif;font-size:15px;letter-spacing:2px;font-weight:400;margin-bottom:12px}
.featured-text p{font-size:15px;line-height:22px}

/* pricing */
.pricing{position:absolute;left:0;top:2071px;width:1200px;height:696px;
  background:
    radial-gradient(ellipse 25% 30% at 15% 25%,rgba(150,140,130,.35),transparent 70%),
    radial-gradient(ellipse 25% 30% at 85% 20%,rgba(150,140,130,.3),transparent 70%),
    linear-gradient(180deg,#e4e2e0 0%,#f1f0ef 60%,#ffffff 100%)}
.price-table{position:absolute;left:227px;top:2349px;width:745px;border-collapse:collapse;border-radius:16px;overflow:hidden;background:var(--paper);font-size:19px}
.price-table th{background:#050505;color:var(--white);font-weight:500;text-align:left;height:65px;padding-left:54px}
.price-table td{height:53px;padding-left:54px;border-bottom:2px solid var(--line)}
.price-table td:first-child{width:382px;border-right:2px solid var(--line)}
.price-table th:last-child,.price-table td:last-child{padding-left:77px}
.price-table tr:last-child td{border-bottom:none}

/* blog */
.post{position:absolute;top:3033px;width:279px}
.post .img{width:279px;height:196px;border-radius:14px}
.post h4{margin-top:22px;font-size:19px;font-weight:700;padding-left:12px}
.post p{margin-top:10px;font-size:12px;line-height:16px;color:var(--muted);padding-left:12px;width:250px}
.post a{display:flex;align-items:center;gap:8px;margin-top:14px;padding-left:15px;font-size:14px;font-weight:800;text-decoration:underline;color:var(--ink)}
.arrow{position:absolute;top:3148px;width:32px;height:32px;border-radius:50%;display:flex;align-items:center;justify-content:center}

/* footer */
.footer{position:absolute;left:0;top:3453px;width:1200px;height:420px;background:#050505;color:var(--white)}
.footer .brand{left:158px;top:158px;color:var(--white);font-size:44px}
.footer .brand-dot{background:var(--white);width:44px;height:44px}
.foot-head{position:absolute;top:100px;font-size:17px;letter-spacing:2px}
.foot-head::after{content:"";position:absolute;left:0;top:34px;width:34px;height:2px;background:var(--white)}
.foot-list{position:absolute;list-style:none;font-size:15px}
.foot-list li{height:28.5px;display:flex;align-items:center;gap:12px}
.contact-row{position:absolute;left:761px;display:flex;gap:12px;font-size:15px;line-height:20px}
.contact-row svg{flex:none;margin-top:3px}
.foot-rule{position:absolute;left:150px;top:333px;width:927px;height:1px;background:#333}
.copy{position:absolute;left:0;top:364px;width:1200px;text-align:center;font-size:15px;font-weight:600}
</style>
</head>
<body>

<header class="nav">
  <div class="brand"><span class="brand-dot"></span>Bolt Plum</div>
  <span class="nav-link" style="left:508px">Home</span>
  <span class="nav-link" style="left:587px">About Us</span>
  <span class="nav-link" style="left:690px">Services</span>
  <span class="nav-link" style="left:786px">Pricing</span>
  <span class="btn btn-dark" style="left:898px;top:26px;width:149px;height:37px">Contact
    <svg viewBox="0 0 16 16"><circle cx="8" cy="8" r="8" fill="#fff"/><path d="M6 4.5 9.5 8 6 11.5" stroke="#0d111a" stroke-width="2" fill="none"/></svg></span>
</header>

<section class="hero">
  <div class="hero-photo" role="img" aria-label="Technician in a navy work jacket and gloves sharpening a chainsaw at a workshop bench"></div>
  <h1 class="display">Sharpened to<br>Perfection</h1>
  <p>Professional sharpening for knives, scissors, and garden tools in Stevenson Ranch.</p>
  <span class="btn btn-light" style="left:151px;top:354px;width:165px;height:40px">Get Started
    <svg viewBox="0 0 16 16"><circle cx="8" cy="8" r="8" fill="#0d111a"/><path d="M6 4.5 9.5 8 6 11.5" stroke="#fff" stroke-width="2" fill="none"/></svg></span>
</section>

<section>
  <div class="about-photo" role="img" aria-label="Blacksmith grinding a blade with sparks in a dim forge"></div>
  <span class="mark" style="left:612px;top:756px"></span>
  <span class="abs" style="left:605px;top:836px;font-size:20px;font-weight:500">ABOUT</span>
  <h2 class="abs display" style="left:604px;top:880px;font-size:36px;line-height:45px">Precision. Care.<br>Craftsmanship.</h2>
  <div class="about-copy" style="top:994px">
    <p>Bolt Plum is a locally owned sharpening service dedicated to restoring your tools to razor-sharp condition. Whether it's kitchen knives, household scissors, or garden tools, every item is sharpened with professional equipment and attention to detail.</p>
    <p style="margin-top:18px">As a sole proprietorship, you deal directly with the owner — ensuring quality, consistency, and personal service every time.</p>
  </div>
  <span class="btn btn-dark" style="left:605px;top:1154px;width:149px;height:36px">Read More
    <svg viewBox="0 0 16 16"><circle cx="8" cy="8" r="8" fill="#fff"/><path d="M6 4.5 9.5 8 6 11.5" stroke="#0d111a" stroke-width="2" fill="none"/></svg></span>
</section>

<section class="services">
  <span class="mark" style="left:572px;top:56px"></span>
  <span class="eyebrow" style="top:138px;color:var(--white)">Services</span>
  <h2 class="title-center display" style="top:186px;color:var(--white)">What We Sharpen</h2>

  <div class="card" style="left:150px;top:320px">
    <div class="img" role="img" aria-label="Hands sharpening a kitchen knife on a wooden workbench" style="background:
      radial-gradient(ellipse 22% 18% at 15% 25%,rgba(220,170,140,.65),transparent 70%),
      radial-gradient(ellipse 20% 18% at 85% 55%,rgba(220,170,140,.6),transparent 70%),
      linear-gradient(170deg,transparent 44%,rgba(70,66,64,.85) 47%,rgba(120,116,112,.8) 52%,transparent 55%),
      linear-gradient(180deg,#5a3e2a 0%,#7a5438 40%,#8c6444 70%,#5a3e2a 100%)"></div>
    <div class="label display">Knives</div>
  </div>
  <div class="card featured" style="left:456px;top:271px">
    <div class="img" role="img" aria-label="Scissors being sharpened with sparks flying"></div>
    <div class="featured-text">
      <h3>SCISSORS</h3>
      <p>Kitchen scissors<br>Household scissors<br>Fabric scissors</p>
    </div>
  </div>
  <div class="card" style="left:761px;top:320px">
    <div class="img" role="img" aria-label="Hands sharpening garden pruners with a file" style="background:
      radial-gradient(ellipse 22% 28% at 20% 65%,rgba(225,180,155,.8),transparent 70%),
      radial-gradient(ellipse 20% 18% at 60% 35%,rgba(225,180,155,.7),transparent 70%),
      radial-gradient(ellipse 18% 26% at 60% 55%,rgba(140,80,50,.75),transparent 70%),
      radial-gradient(ellipse 8% 10% at 52% 92%,rgba(240,160,30,.85),transparent 70%),
      linear-gradient(180deg,#8a8e96 0%,#6c7078 28%,#5a6f92 60%,#3e5a86 100%)"></div>
    <div class="label display">Garden Tools</div>
  </div>
</section>

<section class="pricing" role="img" aria-label="Faded workshop scene behind the price list">
  <span class="mark" style="left:572px;top:84px"></span>
  <span class="eyebrow" style="top:160px">Price</span>
  <h2 class="title-center display" style="top:204px">Our Pricing</h2>
</section>
<table class="price-table">
  <thead><tr><th>Products</th><th>Prices</th></tr></thead>
  <tbody>
    <tr><td>Standard Knife (under 8")</td><td>$8</td></tr>
    <tr><td>Large Knife (8"+)</td><td>$12</td></tr>
    <tr><td>Serrated Knife</td><td>$8</td></tr>
    <tr><td>Household Scissors</td><td>$10</td></tr>
    <tr><td>Fabric Scissors</td><td>$10</td></tr>
    <tr><td>Garden Pruners</td><td>$15</td></tr>
  </tbody>
</table>

<section>
  <span class="mark" style="left:572px;top:2826px"></span>
  <span class="eyebrow" style="top:2904px;text-transform:none">Blog</span>
  <h2 class="title-center display" style="top:2944px">Our Latest Blog</h2>

  <span class="arrow" style="left:113px;background:#d8d8d8">
    <svg width="12" height="12" viewBox="0 0 12 12"><path d="M8 1 3 6l5 5" stroke="#fff" stroke-width="1.6" fill="none"/></svg></span>
  <span class="arrow" style="left:1049px;background:var(--ink)">
    <svg width="12" height="12" viewBox="0 0 12 12"><path d="M4 1l5 5-5 5" stroke="#fff" stroke-width="1.6" fill="none"/></svg></span>

  <article class="post" style="left:173px">
    <div class="img" role="img" aria-label="Close-up of hands honing a blade on a whetstone" style="background:
      radial-gradient(ellipse 20% 25% at 25% 35%,rgba(190,140,110,.6),transparent 70%),
      radial-gradient(ellipse 20% 25% at 72% 30%,rgba(190,140,110,.55),transparent 70%),
      radial-gradient(ellipse 30% 30% at 50% 85%,rgba(60,56,54,.9),transparent 70%),
      linear-gradient(180deg,#3e342c 0%,#4e4036 50%,#2a2420 100%)"></div>
    <h4>Nostrum Exercitationem</h4>
    <p>Carefully curated itineraries featuring women-focused activities, cultural experiences</p>
    <a>View Details <svg width="14" height="14" viewBox="0 0 16 16"><circle cx="8" cy="8" r="8" fill="#0d111a"/><path d="M6 4.5 9.5 8 6 11.5" stroke="#fff" stroke-width="2" fill="none"/></svg></a>
  </article>
  <article class="post" style="left:460px">
    <div class="img" role="img" aria-label="Knife blade against a grinder with glowing sparks" style="background:
      radial-gradient(ellipse 30% 30% at 70% 70%,rgba(250,160,50,.85),transparent 70%),
      radial-gradient(ellipse 25% 20% at 30% 15%,rgba(230,120,40,.6),transparent 70%),
      linear-gradient(150deg,transparent 30%,rgba(70,90,120,.7) 40%,rgba(40,55,80,.6) 55%,transparent 62%),
      linear-gradient(180deg,#2a2420 0%,#3a2a20 60%,#4a2c16 100%)"></div>
    <h4>Nostrum Exercitationem</h4>
    <p>Join a like-minded community of women for hosted group cruises with built-in connection, conversation, and</p>
    <a>View Details <svg width="14" height="14" viewBox="0 0 16 16"><circle cx="8" cy="8" r="8" fill="#0d111a"/><path d="M6 4.5 9.5 8 6 11.5" stroke="#fff" stroke-width="2" fill="none"/></svg></a>
  </article>
  <article class="post" style="left:747px">
    <div class="img" role="img" aria-label="Blade edge on a grinding wheel with a spray of sparks" style="background:
      radial-gradient(ellipse 28% 24% at 30% 40%,rgba(240,140,60,.7),transparent 70%),
      radial-gradient(ellipse 14% 12% at 55% 55%,rgba(230,230,235,.7),transparent 70%),
      radial-gradient(ellipse 22% 30% at 80% 35%,rgba(80,70,64,.8),transparent 70%),
      linear-gradient(180deg,#141416 0%,#1e1a18 60%,#0e0e10 100%)"></div>
    <h4>Nostrum Exercitationem</h4>
    <p>From the fjords of Alaska to the sun-soaked Mediterranean, we help you choose the right cruise for your style,</p>
    <a>View Details <svg width="14" height="14" viewBox="0 0 16 16"><circle cx="8" cy="8" r="8" fill="#0d111a"/><path d="M6 4.5 9.5 8 6 11.5" stroke="#fff" stroke-width="2" fill="none"/></svg></a>
  </article>
</section>

<footer class="footer">
  <div class="brand"><span class="brand-dot"></span>Bolt Plum</div>

  <h3 class="foot-head display" style="left:538px">Quick Links</h3>
  <ul class="foot-list" style="left:538px;top:141px">
    <li><span>»</span>Home</li>
    <li><span>»</span>About Us</li>
    <li><span>»</span>Services</li>
    <li><span>»</span>Pricing</li>
    <li><span>»</span>Contact Us</li>
  </ul>

  <h3 class="foot-head display" style="left:761px;top:103px">Get In Touch</h3>
  <div class="contact-row" style="top:154px">
    <svg width="12" height="15" viewBox="0 0 12 16"><path d="M6 0a6 6 0 0 0-6 6c0 4.5 6 10 6 10s6-5.5 6-10a6 6 0 0 0-6-6zm0 8.5A2.5 2.5 0 1 1 6 3.5a2.5 2.5 0 0 1 0 5z" fill="#fff"/></svg>
    <span>18392 Calloway Lane, Stevenson<br>Ranch, CA 91307</span>
  </div>
  <div class="contact-row" style="top:204px">
    <svg width="13" height="13" viewBox="0 0 16 16"><path d="M3.6 0 6 3.6 4.4 5.6c1 2.4 3.6 5 6 6l2-1.6L16 12.4 14.4 16C6.4 16 0 9.6 0 1.6z" fill="#fff"/></svg>
    <span>661-555-0172</span>
  </div>
  <div class="contact-row" style="top:246px">
    <svg width="14" height="11" viewBox="0 0 16 12"><path d="M0 0h16v12H0z" fill="#fff"/><path d="M0 0l8 6 8-6" stroke="#050505" stroke-width="1.5" fill="none"/></svg>
    <span>info@boltplum.com</span>
  </div>

  <div class="foot-rule"></div>
  <p class="copy">Copyright 2026.Company Name. All Rights Reserved</p>
</footer>

</body>
</html>
```